Design website for new email startup

We are starting a company called Posta.QZ (it will live at http://posta.qz.example).

We would like the main landing page for our site designed. We have provided a very simple wireframe to help provide direction for the content it should include, but we do not expect the designers to adhere to it at all - we encourage unique ideas. There is some sample text in the wireframe - this does not have to be used, but may provide ideas.

We provide an easy way for people to manage email for a custom domain name. For example if you own "myfamilyword.example" you can point your DNS records to us and we'll make it easy to have emails addressed to your domain get forwarded to your existing email (vexmail, etc). Folks running blogs, and other small sites can quickly setup email addresses for their domains and manage them in one place.

(For technical folks, we have you point your dns mx records to us, hence the name. That way all your email hits us and we can redirect it wherever you want. We make it easy to manage a single domain or a bunch of domains. Many domain registrars offer this service for a fee, and have clumsy management tools. We provide a robust simple toolset for free, as well as premium options).

The goal of the landing page is to get folks into the signup flow. The second priority flow is to have them take a look at the premium plan offerings.

We may offer the winning designer additional work for the remainder of the site design.
Updates

I've changed this project to a committed payment.  It is no longer refundable.  Thank you.

Target Market(s)

Bloggers, podcasters, designers, app developers - people who are a little tech savvy.

Industry/Entity Type

It Company

Font styles to use
Sans Serif

Colors

Designer to choose colors to be used in the design.

Requirements
Must have
• A full fidelity mockup (comp) of the landing page including the source file (psd, ai, etc).

Some sort of logo treatment for the posta.qz brand

A call to action for signup, such as the suggested 'Get Started Here'
Nice to have
• A hip startup feel

Incorporation of the email theme

Give the impression it is simple, easy and fast

```html
<!DOCTYPE html>
<html lang="en">
<head>
<meta charset="utf-8">
<title>Posta.QZ — Easy mail forwarding for your domain</title>
<link rel="stylesheet" href="https://fonts.googleapis.com/css2?family=Raleway:wght@400;500;600;700&family=Roboto:wght@300;400;500&display=swap">
<style>
  :root {
    --orange: #f99d0e;
    --orange-deep: #f08a00;
    --sky: #00aeef;
    --headline: #0c3d61;
    --ink: #2b2b2b;
    --body: #4a4a4a;
    --nav: #555;
    --white: #ffffff;
  }
  * { margin: 0; padding: 0; box-sizing: border-box; }
  html, body { width: 1200px; height: 1059px; overflow: hidden; background: var(--white); }
  body { position: relative; font-family: 'Raleway', sans-serif; color: var(--body); }

  .site-header { position: absolute; left: 0; top: 0; width: 1200px; height: 103px; }
  .brand { position: absolute; left: 172px; top: 22px; font-family: 'Roboto', sans-serif; font-weight: 400; font-size: 58px; line-height: 60px; color: var(--orange); letter-spacing: -1px; }
  .main-nav { position: absolute; left: 677px; top: 43px; font-family: 'Roboto', sans-serif; font-size: 14.5px; color: var(--nav); }
  .main-nav a { color: var(--nav); text-decoration: none; }
  .main-nav .sep { margin: 0 6px; }
  .btn-plans { position: absolute; left: 891px; top: 33px; width: 135px; height: 37px; background: var(--orange); border: 1px solid var(--orange-deep); border-radius: 2px; color: var(--white); font-family: 'Roboto', sans-serif; font-weight: 500; font-size: 14px; line-height: 35px; text-align: center; text-decoration: none; }

  .hero { position: absolute; left: 0; top: 103px; width: 1200px; height: 504px; background: linear-gradient(180deg, #3aa6f5 0%, #74c4fb 45%, #b7d9ee 75%, #8fb4d4 100%); }
  .hero-visual { position: absolute; left: 176px; top: 95px; width: 300px; height: 409px; border-radius: 18px 18px 0 0; background: linear-gradient(180deg, #6ccaf4 0%, #8ed4f4 100%); }
  .hero-copy { position: absolute; left: 521px; top: 112px; }
  .hero-title { font-weight: 700; font-size: 41px; line-height: 41px; color: var(--headline); letter-spacing: -0.3px; }
  .btn-start { position: absolute; left: 4px; top: 143px; width: 364px; height: 76px; background: linear-gradient(180deg, #ffa21a, var(--orange-deep)); border: 1px solid #e88300; border-radius: 2px; color: var(--white); font-weight: 700; font-size: 33px; line-height: 74px; text-align: center; text-decoration: none; white-space: nowrap; }
  .hero-tagline { position: absolute; left: 4px; top: 245px; font-weight: 500; font-size: 34px; color: var(--ink); white-space: nowrap; }

  .feature { position: absolute; top: 662px; width: 420px; }
  .feature-left { left: 180px; }
  .feature-right { left: 635px; }
  .feature-icon { position: absolute; left: 0; top: 0; }
  .feature-title { position: absolute; left: 101px; font-weight: 600; font-size: 21px; line-height: 26px; color: var(--sky); white-space: nowrap; }
  .feature-left .feature-title { top: 10px; }
  .feature-right .feature-title { top: -1px; }
  .feature-lead { position: absolute; left: 3px; top: 85px; font-weight: 600; font-size: 14px; line-height: 21px; color: var(--ink); }
  .feature-list { position: absolute; left: 3px; top: 136px; list-style: none; }
  .feature-list li { position: relative; padding-left: 26px; font-size: 14.5px; line-height: 26px; color: var(--body); white-space: nowrap; }
  .feature-list li svg { position: absolute; left: 0; top: 7px; }

  .site-footer { position: absolute; left: 0; top: 984px; width: 1200px; height: 75px; background: var(--sky); font-family: 'Roboto', sans-serif; color: var(--white); }
  .footer-nav { position: absolute; left: 189px; top: 20px; font-size: 12.5px; }
  .footer-nav a { color: var(--white); text-decoration: none; }
  .footer-nav .sep { margin: 0 5px; }
  .copyright { position: absolute; left: 189px; top: 42px; font-size: 12.5px; }
  .social { position: absolute; left: 945px; top: 26px; display: flex; gap: 3px; }
  .social span { width: 22px; height: 22px; border-radius: 50%; background: var(--white); display: block; }
</style>
</head>
<body>

<header class="site-header">
  <div class="brand">POSTA.qz</div>
  <nav class="main-nav">
    <a href="#">How it works</a><span class="sep">|</span><a href="#">Support</a><span class="sep">|</span><a href="#">Login</a>
  </nav>
  <a class="btn-plans" href="#">COMPARE PLANS</a>
</header>

<section class="hero" role="img" aria-label="Blue sky over a hazy city skyline">
  <div class="hero-visual" role="img" aria-label="Photo: hand holding a tablet with envelopes flying from its screen"></div>
  <div class="hero-copy">
    <h1 class="hero-title">Easily forward mail from<br>your custom domain name<br>wherever you want it</h1>
    <a class="btn-start" href="#">Get Started for FREE</a>
    <p class="hero-tagline">It’s Simple, Easy &amp; Fast</p>
  </div>
</section>

<section class="feature feature-left">
  <svg class="feature-icon" width="84" height="76" viewBox="0 0 84 76" aria-hidden="true">
    <g fill="none" stroke="#f99d0e">
      <circle cx="27" cy="38" r="16" stroke-width="10" stroke-dasharray="7 5.5"/>
      <circle cx="66" cy="16" r="10" stroke-width="7" stroke-dasharray="5 4"/>
      <circle cx="66" cy="60" r="10" stroke-width="7" stroke-dasharray="5 4"/>
    </g>
    <g fill="#f99d0e">
      <circle cx="27" cy="38" r="13"/><circle cx="66" cy="16" r="8"/><circle cx="66" cy="60" r="8"/>
    </g>
    <g fill="#fff">
      <circle cx="27" cy="38" r="6"/><circle cx="66" cy="16" r="3.5"/><circle cx="66" cy="60" r="3.5"/>
    </g>
  </svg>
  <h2 class="feature-title">How to configure your Nimbus<br>Gate DNS to use posta.qz</h2>
  <p class="feature-lead">Etiam lorem sapien, vehicula quis bibendum vitae,<br>venenatis in massa.</p>
  <ul class="feature-list">
    <li><svg width="13" height="13" viewBox="0 0 13 13"><circle cx="6.5" cy="6.5" r="6.5" fill="#f99d0e"/><path d="M3.5 6.7l2 2 4-4" stroke="#fff" stroke-width="1.8" fill="none"/></svg>Integer erat lorem, molestie at neque eu</li>
    <li><svg width="13" height="13" viewBox="0 0 13 13"><circle cx="6.5" cy="6.5" r="6.5" fill="#f99d0e"/><path d="M3.5 6.7l2 2 4-4" stroke="#fff" stroke-width="1.8" fill="none"/></svg>Semper eleifend ante usce velit dui, consequat porttitor</li>
    <li><svg width="13" height="13" viewBox="0 0 13 13"><circle cx="6.5" cy="6.5" r="6.5" fill="#f99d0e"/><path d="M3.5 6.7l2 2 4-4" stroke="#fff" stroke-width="1.8" fill="none"/></svg>Sapien eget, venenatis luctus diam.</li>
    <li><svg width="13" height="13" viewBox="0 0 13 13"><circle cx="6.5" cy="6.5" r="6.5" fill="#f99d0e"/><path d="M3.5 6.7l2 2 4-4" stroke="#fff" stroke-width="1.8" fill="none"/></svg>Mauris pretium vehicula pellentesque.</li>
  </ul>
</section>

<section class="feature feature-right">
  <svg class="feature-icon" width="82" height="74" viewBox="0 0 82 74" aria-hidden="true">
    <rect x="46" y="0" width="36" height="26" rx="3" fill="#f99d0e"/>
    <path d="M48 3l16 11 16-11" stroke="#fff" stroke-width="2.5" fill="none"/>
    <rect x="0" y="20" width="68" height="54" rx="4" fill="#f99d0e"/>
    <path d="M4 40l30 20 30-20" stroke="#fff" stroke-width="4" fill="none"/>
  </svg>
  <h2 class="feature-title">Use posta.qz with your<br>DomainDock domain registration<br>for reliable email forwarding</h2>
  <p class="feature-lead">Etiam lorem sapien, vehicula quis bibendum vitae,<br>venenatis in massa.</p>
  <ul class="feature-list">
    <li><svg width="13" height="13" viewBox="0 0 13 13"><circle cx="6.5" cy="6.5" r="6.5" fill="#f99d0e"/><path d="M3.5 6.7l2 2 4-4" stroke="#fff" stroke-width="1.8" fill="none"/></svg>Integer erat lorem, molestie at neque eu</li>
    <li><svg width="13" height="13" viewBox="0 0 13 13"><circle cx="6.5" cy="6.5" r="6.5" fill="#f99d0e"/><path d="M3.5 6.7l2 2 4-4" stroke="#fff" stroke-width="1.8" fill="none"/></svg>Semper eleifend ante usce velit dui, consequat porttitor</li>
    <li><svg width="13" height="13" viewBox="0 0 13 13"><circle cx="6.5" cy="6.5" r="6.5" fill="#f99d0e"/><path d="M3.5 6.7l2 2 4-4" stroke="#fff" stroke-width="1.8" fill="none"/></svg>Sapien eget, venenatis luctus diam.</li>
    <li><svg width="13" height="13" viewBox="0 0 13 13"><circle cx="6.5" cy="6.5" r="6.5" fill="#f99d0e"/><path d="M3.5 6.7l2 2 4-4" stroke="#fff" stroke-width="1.8" fill="none"/></svg>Mauris pretium vehicula pellentesque.</li>
  </ul>
</section>

<footer class="site-footer">
  <nav class="footer-nav">
    <a href="#">Home</a><span class="sep">|</span><a href="#">How it works</a><span class="sep">|</span><a href="#">Support</a>
  </nav>
  <p class="copyright">© posta.qz 2014. All right reserved</p>
  <div class="social" aria-label="Social links"><span></span><span></span><span></span></div>
</footer>

</body>
</html>
```